DriftingLanterns need a podcast cover art that reflects that perspective.

I want a creative(opposite of simple or expected) podcast cover art done relating to the words, "Drifting Lanterns". I want when people to see the cover, for them to think that this is a podcast about thinking....about what we think about...I want it to have a poetic philosophical feel. I want those two words to be clearly seen on there, and I want the primary colors to be white, blue, red.(Haitian Flag colors.)
Look at the uploaded files to get a sense of what I am asking for. God bless.
Drifting Lanterns

```html
<!DOCTYPE html>
<html lang="en">
<head>
<meta charset="utf-8">
<title>Drifting Lanterns — Cover Art</title>
<link rel="stylesheet" href="https://fonts.googleapis.com/css2?family=Yellowtail&family=Bungee&family=Montserrat:wght@400&display=swap">
<style>
  :root {
    --page: #ffffff;
    --paper: #f1f0ec;
    --red: #ed1c24;
    --blue: #0d4f9f;
    --grey: #cbcbcb;
    --ink: #1a1a1a;
    --line: #222222;
  }
  * { margin: 0; padding: 0; box-sizing: border-box; }
  html, body {
    width: 876px;
    height: 1200px;
    overflow: hidden;
    background: var(--page);
  }
  .board {
    position: relative;
    width: 876px;
    height: 1200px;
  }
  .cover {
    position: absolute;
    left: 64px;
    top: 92px;
    width: 744px;
    height: 746px;
    background: var(--paper);
    overflow: hidden;
  }
  .cover__art {
    position: absolute;
    left: 102px;
    top: 300px;
    width: 576px;
    height: 446px;
    border-radius: 48% 52% 0 0 / 40% 44% 0 0;
    background:
      radial-gradient(ellipse at 55% 35%, rgba(237,28,36,0.85), rgba(13,79,159,0.8) 60%, rgba(241,240,236,0) 100%);
  }
  .cover__title-top {
    position: absolute;
    left: 0;
    right: 0;
    top: 20px;
    text-align: center;
    font-family: "Yellowtail", cursive;
    font-size: 190px;
    line-height: 1;
    color: var(--red);
    letter-spacing: -2px;
  }
  .cover__title-bottom {
    position: absolute;
    left: 0;
    right: 0;
    top: 218px;
    text-align: center;
    font-family: "Bungee", sans-serif;
    font-size: 112px;
    line-height: 1;
    color: #ffffff;
    -webkit-text-stroke: 2px var(--ink);
    letter-spacing: 2px;
  }
  .palette-heading {
    position: absolute;
    left: 64px;
    top: 910px;
    width: 744px;
    height: 24px;
  }
  .palette-heading__rule {
    position: absolute;
    top: 11px;
    height: 1px;
    background: var(--line);
  }
  .palette-heading__rule--left { left: 0; width: 236px; }
  .palette-heading__rule--right { right: 0; width: 226px; }
  .palette-heading__label {
    position: absolute;
    left: 0;
    right: 0;
    top: 2px;
    text-align: center;
    font-family: "Montserrat", sans-serif;
    font-size: 15px;
    letter-spacing: 12px;
    padding-left: 12px;
    color: var(--ink);
  }
  .palette {
    position: absolute;
    left: 0;
    top: 1012px;
    width: 876px;
    height: 84px;
  }
  .swatch { position: absolute; top: 0; }
  .swatch--red { left: 137px; }
  .swatch--blue { left: 311px; }
  .swatch--grey { left: 484px; }
  .swatch--white { left: 656px; }
</style>
</head>
<body>
<main class="board">
  <section class="cover">
    <div class="cover__art" role="img" aria-label="Line drawing of a head in profile, the brain rendered as a mosaic of red, blue and white triangles"></div>
    <h1 class="cover__title-top">Drifting</h1>
    <h2 class="cover__title-bottom">LANTERNS</h2>
  </section>

  <div class="palette-heading">
    <span class="palette-heading__rule palette-heading__rule--left"></span>
    <span class="palette-heading__label">COLOR</span>
    <span class="palette-heading__rule palette-heading__rule--right"></span>
  </div>

  <div class="palette">
    <svg class="swatch swatch--red" width="92" height="82" viewBox="0 0 92 82" aria-label="Red swatch">
      <polygon points="46,1 91,81 1,81" fill="var(--red)" stroke="#555" stroke-width="1"/>
    </svg>
    <svg class="swatch swatch--blue" width="92" height="82" viewBox="0 0 92 82" aria-label="Blue swatch">
      <polygon points="1,1 91,1 46,81" fill="var(--blue)"/>
    </svg>
    <svg class="swatch swatch--grey" width="92" height="82" viewBox="0 0 92 82" aria-label="Grey swatch">
      <polygon points="46,1 91,81 1,81" fill="var(--grey)" stroke="#888" stroke-width="1"/>
    </svg>
    <svg class="swatch swatch--white" width="92" height="82" viewBox="0 0 92 82" aria-label="White swatch">
      <polygon points="1,1 91,1 46,81" fill="#ffffff" stroke="#555" stroke-width="1"/>
    </svg>
  </div>
</main>
</body>
</html>
```